Patient Transport company website design

We're a small patient transport company desiring a big company image. Our company is called Pelnorva. We're based in Houston, TX. Our mission is to provide a safe, cost effective, and convenient mode of local transportation. Similar to a taxi service but more patient friendly.
We would like to see designs that illustrate our mission and have a big company online presence. We like bright colors but not too bright and cartoon-like. Our target audience are patients but we also cater to elderly as well as those who might not have reliable transportation.
We're not an emergency transport service. We're not a taxi service. We're more like a shuttle service... a compromise between the two. Photography for the site should show patients and elderly riding in normal (unmarked vehicles) to and from dr visits, etc.
Our competitors' websites are listed here to give you a general idea about the industry.
http://www.trelvanridecare.example/
http://www.brivashuttle.example/
http://www.quomelwayshuttles.example/
Target Market(s)
Patients needing transportation assistance and Elderly as well.
Industry/Entity Type
Taxi
Requirements
Must have
- Website must be done in wordpress. Website must have the following links:
Services, About, Book a trip, jobs, control panel, clients
Should use photos communicating safe travels to and from... particularly with Elderly if possible.
Design should be consistent with attached logo.
Nice to have
- Bright colors

```html
<!DOCTYPE html>
<html lang="en">
<head>
<meta charset="utf-8">
<title>Pelnorva – Patient Transportation Services</title>
<link href="https://fonts.googleapis.com/css2?family=Source+Sans+3:wght@300;400;600&display=swap" rel="stylesheet">
<style>
:root{
  --page-bg:#ededed;
  --white:#ffffff;
  --navy:#0c468c;
  --nav-top:#1a6cb6;
  --nav-bottom:#0b4990;
  --cyan:#1b9ccf;
  --green:#8cc63f;
  --green-dark:#74ad2a;
  --footer:#0d3e84;
  --text:#555a60;
  --muted:#7a7f85;
  --line:#dcdcdc;
}
*{box-sizing:border-box;margin:0;padding:0}
html,body{width:1071px;height:1200px;overflow:hidden}
body{background:var(--page-bg);font-family:"Source Sans 3",sans-serif;color:var(--text);position:relative}
.page{position:absolute;left:89px;top:0;width:908px;height:1100px;background:var(--white)}
.abs{position:absolute}

/* header */
.brand{left:24px;top:34px;display:flex;align-items:center;gap:12px}
.brand-dot{width:40px;height:40px;border-radius:50%;background:var(--green)}
.brand-name{font-size:40px;font-weight:400;color:var(--navy);line-height:1}
.tagline{left:76px;top:78px;font-size:10px;letter-spacing:1.5px;color:var(--cyan);font-style:normal}
.call{right:23px;top:48px;text-align:right}
.call-label{font-size:20px;font-weight:300;color:var(--green);line-height:1}
.call-number{font-size:25px;color:var(--cyan);line-height:1.1}

/* navigation */
.nav{left:0;top:111px;width:908px;height:44px;background:linear-gradient(var(--nav-top),var(--nav-bottom));display:flex}
.nav a{color:var(--white);text-decoration:none;font-size:17px;font-weight:300;line-height:44px;padding:0 21px;border-right:1px solid rgba(0,0,0,.3);box-shadow:1px 0 0 rgba(255,255,255,.15)}
.nav a:last-child{border-right:none;box-shadow:none}

/* hero */
.hero{left:0;top:155px;width:908px;height:341px;background:linear-gradient(180deg,#6d6a64 0%,#c9c7c2 35%,#e8e8e6 55%,#6b6b69 85%,#4a4a48 100%)}
.hero-banner{left:0;top:337px;height:100px}
.hero-title{left:22px;top:355px;font-size:32px;color:var(--white);font-weight:400;line-height:1}
.hero-sub{left:23px;top:394px;font-size:20px;color:var(--white);font-weight:300;line-height:1}
.dots{left:421px;top:472px;display:flex;gap:4px}
.dots span{width:13px;height:13px;border-radius:50%;background:var(--white)}
.dots span.on{background:#b5e61d}

/* feature cards */
.card{top:521px;width:279px;height:255px;border:1px solid var(--line);border-radius:3px;background:var(--white)}
.card-photo{position:absolute;left:16px;top:14px;width:249px;height:118px}
.card-title{position:absolute;left:16px;top:140px;font-size:22px;font-weight:400;line-height:1.1}
.card-text{position:absolute;left:16px;top:168px;width:250px;font-size:11.5px;font-weight:300;line-height:19px;color:var(--muted)}
.btn{position:absolute;left:16px;top:210px;width:87px;height:27px;border-radius:3px;color:var(--white);font-size:13px;text-align:center;line-height:27px}
.c1{left:18px}.c2{left:315px}.c3{left:612px}
.c1 .card-title{color:var(--cyan)}.c1 .btn{background:var(--cyan)}
.c2 .card-title{color:var(--green)}.c2 .btn{background:var(--green)}
.c3 .card-title{color:var(--navy)}.c3 .btn{background:var(--navy)}

/* welcome */
.welcome{left:29px;top:828px;width:566px}
.welcome h1{font-size:28px;font-weight:400;color:var(--navy);line-height:1.1}
.welcome h2{margin-top:10px;font-size:16.5px;font-weight:300;color:#4a4f55}
.welcome p{margin-top:6px;font-size:12.5px;font-weight:300;line-height:21.3px;color:var(--text)}
.welcome p + p{margin-top:9px}

/* services list */
.services{left:612px;top:807px;width:281px;height:237px;border:1px solid var(--line);border-radius:3px;background:linear-gradient(#ffffff 60%,#f1f1f1)}
.services h3{position:absolute;left:31px;top:20px;font-size:25px;font-weight:400;color:var(--green)}
.services ul{position:absolute;left:31px;top:59px;width:213px;list-style:none}
.services li{height:26.6px;border-bottom:1px solid #e3e3e3;display:flex;align-items:center;gap:8px;font-size:12.5px;font-weight:300;color:var(--text)}
.services li:last-child{border-bottom:none}

/* footer */
.footer{left:0;top:1100px;width:1071px;height:100px;background:var(--footer)}
.footer-nav{left:112px;top:22px;font-size:15px;color:var(--white);font-weight:400}
.footer-nav .sep{margin:0 6px;opacity:.8}
.copyright{left:113px;top:50px;font-size:12.5px;font-weight:300;color:#8ea3c4}
.social{left:855px;top:29px;display:flex;gap:7px}
.social span{width:21px;height:21px;border-radius:2px}
</style>
</head>
<body>
<div class="page">
  <header>
    <div class="abs brand"><span class="brand-dot"></span><span class="brand-name">Pelnorva</span></div>
    <div class="abs tagline">Patient Transportation Services</div>
    <div class="abs call">
      <div class="call-label">Call Us Now</div>
      <div class="call-number">555.014.2290</div>
    </div>
  </header>

  <nav class="abs nav">
    <a>Home</a><a>About Us</a><a>Patient Transportation</a><a>Services</a><a>Testimonials</a><a>Hire Us</a><a>Support</a><a>Contact</a>
  </nav>

  <section class="abs hero" role="img" aria-label="Photo of white shuttle buses parked at a hospital entrance"></section>
  <svg class="abs hero-banner" width="560" height="100" viewBox="0 0 560 100" aria-hidden="true">
    <polygon points="0,0 475,0 522,50 475,100 0,100" fill="var(--green)"/>
    <polygon points="475,0 488,0 535,50 488,100 475,100 522,50" fill="var(--cyan)"/>
  </svg>
  <div class="abs hero-title">Patient Transportation Services</div>
  <div class="abs hero-sub">We Provide 24/7 Patient Transportation</div>
  <div class="abs dots"><span class="on"></span><span></span><span></span><span></span></div>

  <article class="abs card c1">
    <div class="card-photo" role="img" aria-label="Photo of attendants helping a patient on a stretcher outside a house" style="background:linear-gradient(135deg,#3f7a5a,#c9c4b8 55%,#4a4a4a)"></div>
    <h3 class="card-title">Cost Effective</h3>
    <p class="card-text">Morbi eget arcu. Morbi porta, libero id ullamcorper nonummy, nibh ligula pulvinar metus</p>
    <a class="btn">Learn More</a>
  </article>
  <article class="abs card c2">
    <div class="card-photo" role="img" aria-label="Photo of a transport van with a patient being loaded" style="background:linear-gradient(135deg,#5d6a4a,#d8d6d0 50%,#6e7a60)"></div>
    <h3 class="card-title">Patient Transportation</h3>
    <p class="card-text">Morbi eget arcu. Morbi porta, libero id ullamcorper nonummy, nibh ligula pulvinar metus</p>
    <a class="btn">Learn More</a>
  </article>
  <article class="abs card c3">
    <div class="card-photo" role="img" aria-label="Photo of two care workers attending a patient" style="background:linear-gradient(135deg,#3e4f6a,#b88a5a 50%,#2c3446)"></div>
    <h3 class="card-title">Provide Safely</h3>
    <p class="card-text">Morbi eget arcu. Morbi porta, libero id ullamcorper nonummy, nibh ligula pulvinar metus</p>
    <a class="btn">Learn More</a>
  </article>

  <section class="abs welcome">
    <h1>Welcome to Our Website Mainpage..</h1>
    <h2>Proin nulla arcu nonummy luctus dictum eget fermentum et lorem</h2>
    <p>Duis tincidunt lectus quis dui viverra vestibulum. Suspendisse vulputate aliquam dui. Nulla elementum dui ut augue. Aliquam vehicula mi at mauris. Maecenas placerat, nisl at consequat rhoncus, sem nunc gravida justo, quis eleifend arcu velit quis lacus. Morbi magna magna, tincidunt a, mattis non, imperdiet vitae, tellus. Sed odio est, auctor ac, sollicitudin in, consequat vitae, orci.</p>
    <p>Donec scelerisque leo ac risus. Praesent sit amet est. In dictum, dolor eu dictum porttitor, enim felis viverra mi, eget luctus massa purus quis odio. Etiam nulla massa, pharetra facilisis, volutpat in</p>
  </section>

  <aside class="abs services">
    <h3>Services We Provide</h3>
    <ul>
      <li><svg width="17" height="17" viewBox="0 0 17 17"><circle cx="8.5" cy="8.5" r="8.5" fill="var(--green)"/><path d="M4.5 8.8l2.8 2.7 5.2-5.6" fill="none" stroke="#fff" stroke-width="2"/></svg>Vivamus porttitor nisi eleifend</li>
      <li><svg width="17" height="17" viewBox="0 0 17 17"><circle cx="8.5" cy="8.5" r="8.5" fill="var(--green)"/><path d="M4.5 8.8l2.8 2.7 5.2-5.6" fill="none" stroke="#fff" stroke-width="2"/></svg>Libero tempus libero lectus feugiat</li>
      <li><svg width="17" height="17" viewBox="0 0 17 17"><circle cx="8.5" cy="8.5" r="8.5" fill="var(--green)"/><path d="M4.5 8.8l2.8 2.7 5.2-5.6" fill="none" stroke="#fff" stroke-width="2"/></svg>Morbi diam mauris viverra</li>
      <li><svg width="17" height="17" viewBox="0 0 17 17"><circle cx="8.5" cy="8.5" r="8.5" fill="var(--green)"/><path d="M4.5 8.8l2.8 2.7 5.2-5.6" fill="none" stroke="#fff" stroke-width="2"/></svg>Morbi eget arcu</li>
      <li><svg width="17" height="17" viewBox="0 0 17 17"><circle cx="8.5" cy="8.5" r="8.5" fill="var(--green)"/><path d="M4.5 8.8l2.8 2.7 5.2-5.6" fill="none" stroke="#fff" stroke-width="2"/></svg>Morbi porta libero id ullamcorper</li>
      <li><svg width="17" height="17" viewBox="0 0 17 17"><circle cx="8.5" cy="8.5" r="8.5" fill="var(--green)"/><path d="M4.5 8.8l2.8 2.7 5.2-5.6" fill="none" stroke="#fff" stroke-width="2"/></svg>Ligula pulvinar metus eget</li>
    </ul>
  </aside>
</div>

<footer class="abs footer">
  <div class="abs footer-nav">Home<span class="sep">|</span>About Us<span class="sep">|</span>Patient Transportation<span class="sep">|</span>Services<span class="sep">|</span>Testimonials<span class="sep">|</span>Hire Us<span class="sep">|</span>Support<span class="sep">|</span>Contact</div>
  <div class="abs copyright">Copyright © 2013 Company Name.&nbsp; All right reserved</div>
  <div class="abs social">
    <span style="background:#3b5b98"></span>
    <span style="background:#33aee0"></span>
    <span style="background:#1877b5"></span>
    <span style="background:#f39021"></span>
  </div>
</footer>
</body>
</html>
```